Business Management Fortress

Assist with enhancing a powerpoint slide by providing a few design options for consideration. I have a template but open to any creative ideas.

Target Market(s)

Internal employees and stakeholders

Industry/Entity Type

Business Management, Finance, Accounting

Requirements
Must have
• Maintain a fortress, temple, or pyramid schema
Nice to have
• Scenic Background

```html
<!DOCTYPE html>
<html lang="en">
<head>
<meta charset="utf-8">
<title>Business Management Fortress</title>
<link href="https://fonts.googleapis.com/css2?family=Carlito:wght@400;700&display=swap" rel="stylesheet">
<style>
  :root {
    --sky-top: #4f6f9e;
    --sky-mid: #7f97b8;
    --mountain: #4a5f86;
    --mist: #c9ccd3;
    --mist-low: #b9bbc2;
    --stone: rgba(240, 243, 248, 0.86);
    --stone-soft: rgba(236, 240, 246, 0.72);
    --ink: #111418;
    --title: #ffffff;
    --divider: #9aa6b6;
  }
  html, body {
    margin: 0;
    padding: 0;
    width: 1200px;
    height: 675px;
    overflow: hidden;
  }
  .slide {
    position: relative;
    width: 1200px;
    height: 675px;
    font-family: "Carlito", "Calibri", sans-serif;
  }
  .scenery {
    position: absolute;
    inset: 0;
    background:
      linear-gradient(180deg, transparent 0%, transparent 44%, var(--mountain) 52%, rgba(120,135,165,0.9) 62%, var(--mist) 70%, var(--mist-low) 100%),
      linear-gradient(180deg, var(--sky-top) 0%, var(--sky-mid) 40%, #a9b6c9 50%);
  }
  .slide-title {
    position: absolute;
    left: 67px;
    top: 58px;
    margin: 0;
    font-size: 40px;
    font-weight: 700;
    color: var(--title);
    letter-spacing: 0.2px;
  }
  .fortress {
    position: absolute;
    inset: 0;
  }
  .stone { fill: var(--stone); }
  .stone-soft { fill: var(--stone-soft); }
  .divider { stroke: var(--divider); stroke-width: 1; }
  .label {
    font-family: "Carlito", "Calibri", sans-serif;
    fill: var(--ink);
    text-anchor: middle;
  }
  .label-roof { font-size: 21px; font-weight: 700; letter-spacing: 0.3px; }
  .label-pillar { font-size: 23px; font-weight: 700; }
  .label-base { font-size: 22px; font-weight: 700; }
  .label-duties { font-size: 22px; font-weight: 400; }
</style>
</head>
<body>
<div class="slide">
  <div class="scenery" role="img" aria-label="Snow-capped mountain range above a sea of clouds under a blue sky"></div>
  <h1 class="slide-title">Business Management Fortress</h1>

  <svg class="fortress" width="1200" height="675" viewBox="0 0 1200 675" aria-label="Fortress diagram">
    <!-- roof -->
    <polygon class="stone-soft" points="66,240 600,195 1134,240"/>
    <rect class="stone" x="66" y="240" width="1068" height="43"/>
    <line class="divider" x1="437" y1="237" x2="437" y2="275"/>
    <line class="divider" x1="762" y1="237" x2="762" y2="275"/>
    <text class="label label-roof" x="275" y="264">LEADER</text>
    <text class="label label-roof" x="600" y="264">PARTNER</text>
    <text class="label label-roof" x="925" y="264">PROFITABILITY</text>

    <!-- architrave -->
    <rect class="stone-soft" x="100" y="286" width="999" height="34"/>

    <!-- pillars -->
    <g class="pillar" transform="translate(100,0)">
      <rect class="stone-soft" x="0" y="323" width="207" height="18"/>
      <rect class="stone-soft" x="18" y="343" width="171" height="12"/>
      <rect class="stone-soft" x="33" y="358" width="141" height="12"/>
      <rect class="stone" x="33" y="372" width="141" height="108"/>
      <rect class="stone" x="33" y="482" width="141" height="12"/>
      <rect class="stone" x="18" y="496" width="171" height="12"/>
      <rect class="stone" x="0" y="510" width="207" height="18"/>
      <text class="label label-pillar" x="103.5" y="434">People</text>
    </g>
    <g class="pillar" transform="translate(364,0)">
      <rect class="stone-soft" x="0" y="323" width="207" height="18"/>
      <rect class="stone-soft" x="18" y="343" width="171" height="12"/>
      <rect class="stone-soft" x="33" y="358" width="141" height="12"/>
      <rect class="stone" x="33" y="372" width="141" height="108"/>
      <rect class="stone" x="33" y="482" width="141" height="12"/>
      <rect class="stone" x="18" y="496" width="171" height="12"/>
      <rect class="stone" x="0" y="510" width="207" height="18"/>
      <text class="label label-pillar" x="103.5" y="434">Innovation</text>
    </g>
    <g class="pillar" transform="translate(628,0)">
      <rect class="stone-soft" x="0" y="323" width="207" height="18"/>
      <rect class="stone-soft" x="18" y="343" width="171" height="12"/>
      <rect class="stone-soft" x="33" y="358" width="141" height="12"/>
      <rect class="stone" x="33" y="372" width="141" height="108"/>
      <rect class="stone" x="33" y="482" width="141" height="12"/>
      <rect class="stone" x="18" y="496" width="171" height="12"/>
      <rect class="stone" x="0" y="510" width="207" height="18"/>
      <text class="label label-pillar" x="103.5" y="419">Business</text>
      <text class="label label-pillar" x="103.5" y="449">Intelligence</text>
    </g>
    <g class="pillar" transform="translate(892,0)">
      <rect class="stone-soft" x="0" y="323" width="207" height="18"/>
      <rect class="stone-soft" x="18" y="343" width="171" height="12"/>
      <rect class="stone-soft" x="33" y="358" width="141" height="12"/>
      <rect class="stone" x="33" y="372" width="141" height="108"/>
      <rect class="stone" x="33" y="482" width="141" height="12"/>
      <rect class="stone" x="18" y="496" width="171" height="12"/>
      <rect class="stone" x="0" y="510" width="207" height="18"/>
      <text class="label label-pillar" x="103.5" y="419">Strategic</text>
      <text class="label label-pillar" x="103.5" y="449">Alliances</text>
    </g>

    <!-- foundation -->
    <rect class="stone" x="66" y="532" width="1068" height="33"/>
    <text class="label label-base" x="596" y="556">Fiduciary Responsibilities</text>
    <rect class="stone" x="66" y="569" width="1068" height="65"/>
    <text class="label label-duties" x="597" y="608">Accurate Financials / Internal Controls / Brand Protection / Compliance / Ethics / Cost Management</text>
  </svg>
</div>
</body>
</html>
```